A5 Flyer for Financial Services Business

I am after a re-design of our business flyer to fit in with our new branding style and logo colour scheme. Wanting something with a bit of designer flair that I could not create myself. I have included the flyer which I created which lacks style so dazzle me.

I want to use the same content.

Text for main body of flyer is

Are you a small business owner, tradie or PAVC Service Provider struggling to stay on top of your bookkeeping and compliance obligations? If so we would love to help you get back on track and take control of your business finances so that you can make informed business decisions and focus on what you do best.

We have over 20 years industry experience and, as a small business ourselves, we are able to offer our clients a personal bookkeeping solution tailored to meet the needs of your business.

Accounts Payable | Accounts Receivable
Customer Invoicing
Bank and Credit Card Reconciliations
Payroll | Superannuation | Payroll Tax
Business Activity | Instalment Activity Statements
Regular Financial Reports
Ledgerly and BookNest Set-Up and Training

```html
<!DOCTYPE html>
<html lang="en">
<head>
<meta charset="utf-8">
<title>Even Keel Financial Services – Bookkeeping Flyer</title>
<link href="https://fonts.googleapis.com/css2?family=Federo&family=Montserrat:wght@300&family=Poppins:ital,wght@0,500;1,400;1,600;1,800&family=Oswald:wght@500&family=Marcellus&display=swap" rel="stylesheet">
<style>
  :root{
    --teal:#0b9f99;
    --navy:#0e4a66;
    --lime:#c9d32b;
    --ink:#111;
    --white:#fff;
    --brand:#1d6f86;
    --photo-a:#2b2d30;
    --photo-b:#6f7378;
  }
  *{margin:0;padding:0;box-sizing:border-box}
  html,body{width:846px;height:1200px;overflow:hidden;background:var(--white)}
  .flyer{position:relative;width:846px;height:1200px;overflow:hidden;background:var(--white);font-family:"Poppins",sans-serif;color:var(--ink)}
  .shapes{position:absolute;inset:0}
  .brand-disc{position:absolute;left:-3px;top:-82px;width:424px;height:398px;border-radius:50%;background:var(--white)}
  .brand-name{position:absolute;left:30px;top:154px;width:360px;font-family:"Montserrat",sans-serif;font-weight:300;color:var(--brand);text-align:center}
  .brand-name .line1{display:block;font-size:37px;letter-spacing:1px;line-height:1}
  .brand-name .line2{display:block;font-size:20px;letter-spacing:10px;margin-top:8px}
  .headline{position:absolute;left:0;top:0;font-family:"Federo",sans-serif;color:var(--white);font-weight:400}
  .headline span{position:absolute;white-space:nowrap;font-size:60px;line-height:1;transform-origin:left center}
  .headline .l1{left:16px;top:390px;transform:rotate(9deg)}
  .headline .l2{left:16px;top:456px;transform:rotate(12deg)}
  .headline .l3{left:22px;top:524px;transform:rotate(13deg)}
  .intro{position:absolute;left:12px;top:650px;width:470px}
  .intro .lead{font-style:italic;font-size:17px;line-height:1.3}
  .intro .audience{font-style:italic;font-weight:800;font-size:32px;line-height:32px;color:var(--teal);margin:2px 0 4px}
  .intro .body{font-style:italic;font-size:17px;line-height:25.6px}
  .intro .body strong{font-weight:800;font-size:19px}
  .experience{position:absolute;left:12px;top:955px;width:470px;font-style:italic;font-size:17px;line-height:25.6px;font-weight:500}
  .experience strong{font-weight:800;font-size:22px}
  .certs{position:absolute;top:1074px;left:22px;display:flex;gap:48px}
  .cert{display:flex;align-items:center;gap:6px}
  .cert .diamond{width:23px;height:23px;transform:rotate(45deg)}
  .cert .label{color:var(--white);font-size:12.5px;font-weight:500;padding:2px 5px}
  .cert.teal .diamond,.cert.teal .label{background:var(--teal)}
  .cert.navy .diamond,.cert.navy .label{background:var(--navy)}
  .footer-band{position:absolute;left:0;top:1108px;width:846px;height:92px;background:var(--teal)}
  .contact{position:absolute;left:14px;color:var(--white);display:flex;align-items:center;gap:8px}
  .contact.phone{top:1118px;font-family:"Oswald",sans-serif;font-size:30px;font-weight:500}
  .contact.web{top:1158px;font-size:18px;font-weight:500}
  .services-title{position:absolute;left:524px;top:588px;width:310px;height:66px;background:var(--navy);border:1px solid var(--lime);border-radius:8px;color:var(--white);font-family:"Marcellus",serif;font-size:44px;text-align:center;line-height:66px;letter-spacing:-1px}
  .services{position:absolute;left:524px;top:664px;width:310px;height:499px;background:var(--navy);border:1px solid var(--lime);border-radius:10px;padding:18px 0 0 22px;list-style:none;color:var(--white)}
  .services li{font-style:italic;font-weight:600;font-size:21.5px;line-height:32px;white-space:nowrap}
  .services li .cont{display:block;padding-left:36px}
</style>
</head>
<body>
<div class="flyer">
  <svg class="shapes" width="846" height="1200" viewBox="0 0 846 1200">
    <defs>
      <linearGradient id="photoTone" x1="0" y1="0" x2="1" y2="1">
        <stop offset="0" stop-color="#3a3c40"/>
        <stop offset=".6" stop-color="#5c6066"/>
        <stop offset="1" stop-color="#8a8e93"/>
      </linearGradient>
    </defs>
    <rect x="0" y="0" width="846" height="560" fill="url(#photoTone)" role="img" aria-label="Photo of a smiling accountant in a pinstripe suit with arms crossed, in front of a desk with a laptop showing plans"/>
    <path d="M0,362 C170,330 330,350 440,430 C520,490 600,560 846,440 L846,880 L524,880 L524,1108 L0,1108 Z" fill="var(--teal)"/>
    <path d="M0,645 C170,590 360,620 524,802 L524,1108 L0,1108 Z" fill="var(--white)"/>
    <circle cx="698" cy="366" r="76" fill="var(--lime)" role="img" aria-label="Registration badge"/>
  </svg>

  <div class="brand-disc"></div>
  <div class="brand-name">
    <span class="line1">EVEN KEEL</span>
    <span class="line2">Financial Services</span>
  </div>

  <h1 class="headline">
    <span class="l1">BookKeeping</span>
    <span class="l2">Tailored to your</span>
    <span class="l3">Business Needs</span>
  </h1>

  <section class="intro">
    <p class="lead">Are you a</p>
    <p class="audience">Small Business<br>owner,tradie or<br>PAVC Service Provider</p>
    <p class="body">struggling to stay on top of your<br><strong>bookkeeping and compliance obligations?</strong><br>If so we would love to help you get back on track and take control of your business finances so that you can make informed business decisions and focus on what you do best.</p>
  </section>

  <p class="experience">We have over <strong>20 years industry experience</strong> and, as a small business ourselves, we are able to offer our clients a personal bookkeeping solution tailored to meet the needs of your business.</p>

  <div class="certs">
    <div class="cert teal"><span class="diamond"></span><span class="label">Ledgerly Certified Advisor</span></div>
    <div class="cert navy"><span class="diamond"></span><span class="label">BookNest Certified Advisor</span></div>
  </div>

  <div class="footer-band"></div>
  <div class="contact phone">
    <svg width="36" height="28" viewBox="0 0 36 28" aria-hidden="true"><path d="M2,10 C2,3 34,3 34,10 L34,13 L26,13 L26,9 L10,9 L10,13 L2,13 Z" fill="#fff"/><rect x="8" y="14" width="20" height="13" rx="2" fill="#fff"/></svg>
    0400 318 762
  </div>
  <div class="contact web">
    <svg width="22" height="22" viewBox="0 0 22 22" aria-hidden="true"><circle cx="11" cy="11" r="9" fill="none" stroke="#fff" stroke-width="2"/><ellipse cx="11" cy="11" rx="4" ry="9" fill="none" stroke="#fff" stroke-width="1.6"/><path d="M2,11 H20 M4,6 H18 M4,16 H18" stroke="#fff" stroke-width="1.4"/></svg>
    www.evenkeelfinancial.com.au
  </div>

  <h2 class="services-title">SERVICES</h2>
  <ol class="services">
    <li>1. Accounts Payable</li>
    <li>2. Accounts Receivable</li>
    <li>3. Customer Invoicing</li>
    <li>4. Bank and Credit</li>
    <li>5. Card Reconciliations</li>
    <li>6. Payroll</li>
    <li>7. Superannuation</li>
    <li>8. Payroll Tax</li>
    <li>9. Business Activity</li>
    <li>10.Instalment Activity<span class="cont">Statements</span></li>
    <li>11. Regular Financial<span class="cont">Reports</span></li>
    <li>12. Ledgerly and BookNest<span class="cont">Set-Up and Training</span></li>
  </ol>
</div>
</body>
</html>
```